IV Nutritional Clinic Web Design

We are working with Velmo. They are an IV Nutritional Clinic and in need of a new website design.
Some sites to use for inspiration:
https://brantlowcare.example
https://www.zolvarihealth.example
https://www.quellspa.example
https://pimrolift.example
https://www.dorvak-well.example/pages/iv-therapy-west-hollywood
https://www.tqoncowell.example/cancer-care/iv-drips/
https://drelmavita.example
https://salbrikmed.example
Thank you for taking the time to consider designing a website for us. We are web developers based in Stockton, CA, USA. Most of our projects go through the same process. Understanding this process may help you win a project with us. We custom-code all of our websites in-house. We don’t have any requirements as to what tools you use for your design, but we prefer Figma files. For any design that we label as four-stars, we send it to the client for review. The client picks the final design they want us to use. Once we complete this process, we will continue to show additional clients all the four-star sites and purchase them later. Your designs will have multiple chances to sell. For better chances of success, we ask that you follow these guidelines.
IMAGES:
If you use any images or icons in the design, we ask that you have a link to the asset so we can purchase the image/icon. Most of the designs we submit do not have the customer’s images on them unless they have some great images. Be creative; show us the feeling you are trying to portray with your image choices. Use any royalty-free site you choose. We subscribe to Corvix and mainly use their images, but we can purchase images outside of Corvix.
PLEASE NOTE: we will not submit designs to clients with watermarks on the images.
FONTS:
We ask that you identify the fonts used in the design. This can be done in a message if you want. We typically use Lumen Typeset and Corvix Fonts.
CONTENT:
We're always open to different content and ideas. We often submit designs with stock images so the client can see our vision. We typically take pictures after the website launch to use their images with our vision. Lorem Ipsum is fine for paragraphs, but we ask that you write the headers in correct English. We want to be able to show the vision and identify the sections of the website.
INSPIRATION:
We typically add a couple of links in the brief of websites we like to help you get started in your design.
REVISIONS:
We do not often ask for revisions of the designs unless we see something in the design that may not appeal to the client. If there are slight changes that we want to make, we do that in the development process.
FEEDBACK:
We rarely give feedback on designs during the design process. We are working on many website projects and do not have the time to provide feedback. We usually respond if your request is well thought out and asks specific questions, but a note asking “feedback, please” usually goes unanswered.
Number of Pages Required
1 page
Look and feel
Each slider illustrates characteristics of the customer's brand and the style your logo design should communicate.

```html
<!DOCTYPE html>
<html lang="en">
<head>
<meta charset="utf-8">
<title>Velmo Hydration – IV Nutrition Clinic</title>
<link href="https://fonts.googleapis.com/css2?family=Poppins:wght@400;500;600;700&display=swap" rel="stylesheet">
<style>
:root{
  --blue:#1f3b9b;
  --blue-deep:#18307f;
  --green:#8dc356;
  --green-soft:#f5fbec;
  --green-line:#b9de90;
  --ink:#1d1d1d;
  --text:#3a3a3a;
  --muted:#f6f6f6;
  --footer:#3b3b3b;
  --white:#ffffff;
}
*{box-sizing:border-box;margin:0;padding:0}
html,body{width:1200px;height:5213px;overflow:hidden}
body{font-family:'Poppins',sans-serif;color:var(--text);background:var(--white);position:relative}
section,header,footer{position:absolute;left:0;width:1200px}
.abs{position:absolute}
.btn{position:absolute;display:flex;align-items:center;justify-content:center;gap:10px;font-size:13px;font-weight:500;color:var(--white);border-radius:3px}
.btn-green{background:var(--green)}
.btn-blue{background:var(--blue)}
.btn svg{width:14px;height:14px}
.section-title{position:absolute;left:0;width:1200px;text-align:center;font-size:30px;font-weight:600;color:var(--ink)}
.section-title em{font-style:normal;color:var(--green)}

/* header */
.site-header{top:0;height:93px;background:var(--white)}
.brand{position:absolute;display:flex;align-items:center;gap:10px;font-weight:700;font-size:30px;color:var(--blue)}
.brand i{display:block;width:16px;height:16px;background:var(--green)}
.nav a{position:absolute;top:40px;font-size:13px;color:var(--ink);text-decoration:none}
.nav a.active{color:var(--green);font-weight:500}

/* hero */
.hero{top:93px;height:648px;background:var(--blue)}
.hero h1{position:absolute;left:82px;top:186px;font-size:41px;line-height:48px;font-weight:600;color:var(--white)}
.hero h1 em{font-style:normal;color:var(--green)}
.hero p{position:absolute;left:82px;top:360px;width:440px;font-size:15px;line-height:25px;color:var(--white)}

/* why */
.why{top:741px;height:716px}
.why .lead{position:absolute;left:300px;top:160px;width:600px;text-align:center;font-size:15px;line-height:25px;color:var(--ink)}
.why-card{position:absolute;top:317px;height:348px;background:var(--muted);text-align:center}
.why-card.featured{top:307px;height:358px;background:var(--green-soft);border:2px solid var(--green-line);border-radius:4px}
.why-card .tag{position:absolute;left:50%;top:-20px;margin-left:-40px;width:80px;height:92px}
.why-card .num{position:absolute;right:18px;top:20px;font-size:44px;font-weight:700;color:transparent;-webkit-text-stroke:1.5px var(--green-line)}
.why-card h3{position:absolute;left:0;right:0;top:118px;font-size:16px;font-weight:600;color:var(--ink)}
.why-card p{position:absolute;left:30px;right:30px;top:158px;font-size:13px;line-height:25px;color:var(--ink)}

/* nourish */
.nourish{top:1508px;height:500px}
.nourish h2{position:absolute;left:581px;top:140px;font-size:30px;line-height:46px;font-weight:600;color:var(--ink)}
.nourish h2 em{font-style:normal;color:var(--white)}
.nourish p{position:absolute;left:581px;top:250px;width:500px;font-size:12.5px;line-height:22px;color:var(--ink)}

/* treatments */
.treatments{top:2008px;height:961px}
.treat{position:absolute;width:300px}
.treat .ico{width:88px;height:88px;border-radius:50%;background:var(--blue);display:flex;align-items:center;justify-content:center}
.treat .ico svg{width:40px;height:40px}
.treat h3{margin-top:30px;font-size:16px;font-weight:600;color:var(--ink);line-height:24px;width:240px}
.treat p{margin-top:10px;font-size:12.5px;line-height:19px;color:var(--ink);width:240px}
.treat .more{margin-top:12px;font-size:12px;color:var(--green);display:flex;align-items:center;gap:6px}
.treat-feature{position:absolute;left:403px;top:178px;width:338px;height:287px;background:var(--green-soft)}
.vline{position:absolute;width:1px;background:#d9d9d9}
.cta-line{position:absolute;left:144px;top:809px;width:910px;height:1px;background:#d9d9d9}
.cta-text{position:absolute;left:146px;top:860px;font-size:27px;font-weight:600;color:var(--blue)}

/* benefits */
.benefits{top:2969px;height:599px;background:var(--blue)}
.benefits h2{position:absolute;left:636px;top:62px;font-size:30px;font-weight:600;color:var(--white)}
.benefits h2 em{font-style:normal;color:var(--green)}
.benefits .intro{position:absolute;left:636px;top:120px;width:440px;font-size:12.5px;line-height:20px;color:#dfe5f8}
.acc{position:absolute;left:636px;width:446px;border-bottom:1px solid rgba(255,255,255,.45);display:flex;justify-content:space-between;align-items:center;font-size:19px;font-weight:500;color:var(--white);height:44px}
.acc.open{color:var(--green)}
.acc svg{width:16px;height:16px}
.acc-body{position:absolute;left:636px;top:282px;width:446px;font-size:12.5px;line-height:21px;color:#dfe5f8}

/* testimonials */
.testimonials{top:3568px;height:560px;background:var(--white)}
.t-card{position:absolute;top:170px;width:306px;height:229px;background:var(--white);box-shadow:0 6px 24px rgba(0,0,0,.10);padding:24px}
.t-top{display:flex;justify-content:space-between;align-items:center}
.stars{color:var(--green);font-size:16px;letter-spacing:2px}
.t-badge{display:flex;align-items:center;gap:5px;font-size:10px;font-weight:600;color:var(--ink)}
.t-badge i{width:11px;height:11px;border-radius:50%;background:var(--blue);display:block}
.t-card p{margin-top:18px;font-size:12.5px;line-height:19px;color:var(--ink)}
.t-author{position:absolute;left:24px;bottom:28px;display:flex;align-items:center;gap:8px;font-size:11px;font-weight:600;color:var(--ink)}
.t-author i{width:26px;height:26px;border-radius:50%;background:linear-gradient(135deg,#b9a396,#6b5c55);display:block}
.arrow{position:absolute;top:260px;width:24px;height:36px}

/* contact */
.contact{top:4128px;height:672px}
.contact h2{position:absolute;left:111px;top:134px;font-size:30px;line-height:44px;font-weight:600;color:var(--green)}
.contact h2 span{color:var(--ink)}
.contact h4{position:absolute;left:111px;top:280px;font-size:16px;font-weight:600;color:var(--ink)}
.info{position:absolute;display:flex;gap:12px;font-size:13px;line-height:20px;color:var(--ink)}
.info svg{width:18px;height:18px;flex:none;margin-top:2px}
.form-box{position:absolute;left:577px;top:104px;width:516px;height:568px;background:var(--green)}
.form-box h3{position:absolute;left:73px;top:50px;font-size:26px;line-height:40px;font-weight:500;color:var(--white)}
.field{position:absolute;left:66px;width:387px;height:44px;background:var(--white);font-size:13px;color:var(--ink);padding:13px 18px}
.footer .dim{color:#d8d8d8}

/* footer */
.footer{top:4800px;height:413px;background:var(--footer);color:var(--white)}
.footer h5{position:absolute;font-size:14px;font-weight:600;letter-spacing:.5px}
.footer .link{position:absolute;left:498px;font-size:13px}
.social{position:absolute;top:212px;left:117px;display:flex;gap:14px}
.social i{width:24px;height:24px;border-radius:50%;background:var(--white);display:block}
.footer .rule{position:absolute;left:95px;top:323px;width:1020px;height:1px;background:#6a6a6a}
.footer .copy{position:absolute;left:0;width:1200px;top:352px;text-align:center;font-size:12px}
</style>
</head>
<body>

<header class="site-header">
  <div class="brand" style="left:83px;top:24px">Velmo<i></i></div>
  <nav class="nav">
    <a class="active" style="left:441px">Home</a>
    <a style="left:520px">About Us</a>
    <a style="left:617px">Treatment</a>
    <a style="left:725px">Treatments</a>
    <a style="left:840px">Contact</a>
  </nav>
  <div class="btn btn-green" style="left:943px;top:32px;width:172px;height:35px;font-size:12.5px">Schedule Appointment</div>
</header>

<section class="hero">
  <svg class="abs" style="left:0;top:0" width="1200" height="648" viewBox="0 0 1200 648">
    <defs>
      <linearGradient id="heroPhoto" x1="0" y1="0" x2="1" y2="1">
        <stop offset="0" stop-color="#dfe6ee"/><stop offset=".55" stop-color="#f1f3f6"/><stop offset="1" stop-color="#c9cfd8"/>
      </linearGradient>
    </defs>
    <polygon points="690,0 574,320 690,648 712,648 598,320 712,0" fill="var(--green)"/>
    <polygon points="712,0 1200,0 1200,648 712,648 598,320" fill="url(#heroPhoto)" role="img" aria-label="Photo of a smiling woman in a white robe receiving an IV drip from a clinician in pink gloves"/>
  </svg>
  <h1><em>Supercharge your<br>hydration &amp; wellness</em><br>with Velmo Hydration</h1>
  <p>Get vitamins directly into your bloodstream with intravenous micronutrient therapy and boosters.</p>
  <div class="btn btn-green" style="left:82px;top:459px;width:170px;height:37px">Book Appointment
    <svg viewBox="0 0 16 16" fill="none" stroke="#fff" stroke-width="1.6"><path d="M2 8h11M9 4l4 4-4 4"/></svg></div>
</section>

<section class="why">
  <h2 class="section-title" style="top:102px">Why Choose <em>Velmo Hydration?</em></h2>
  <p class="lead">Intravenous Nutrient Therapy, also known as IV Drips, and boosters, are an alternative approach to oral supplements that delivers nutrients directly into the bloodstream.</p>

  <div class="why-card" style="left:83px;width:336px">
    <svg class="tag" viewBox="0 0 80 92"><polygon points="0,0 80,0 80,76 40,92 0,76" fill="var(--green)"/><g fill="none" stroke="#fff" stroke-width="2.2"><path d="M40 28c-5 6-5 14 0 20 5-6 5-14 0-20z"/><path d="M26 36c0 8 6 12 14 12s14-4 14-12"/></g></svg>
    <div class="num">01</div>
    <h3>Effective Results</h3>
    <p>Lorem ipsum dolor sit amet consectetur. Habitant venenatis sit laoreet faucibus semper ornare viverra senectus. Bibendum senectus nunc nec id enim tincidunt ut dictum.</p>
  </div>
  <div class="why-card featured" style="left:435px;width:332px">
    <svg class="tag" viewBox="0 0 80 92"><polygon points="0,0 80,0 80,76 40,92 0,76" fill="var(--green)"/><g fill="none" stroke="#fff" stroke-width="2.2"><rect x="28" y="24" width="24" height="30" rx="3"/><path d="M32 34l3 3 5-5M32 45l3 3 5-5M44 35h4M44 46h4"/></g></svg>
    <div class="num">02</div>
    <h3 style="top:128px">Personalised Plans</h3>
    <p style="top:168px">Lorem ipsum dolor sit amet consectetur. Habitant venenatis sit laoreet faucibus semper ornare viverra senectus. Bibendum senectus nunc nec id enim tincidunt ut dictum.</p>
  </div>
  <div class="why-card" style="left:783px;width:334px">
    <svg class="tag" viewBox="0 0 80 92"><polygon points="0,0 80,0 80,76 40,92 0,76" fill="var(--green)"/><circle cx="40" cy="38" r="14" fill="#fff"/><path d="M33 38l5 5 9-9" fill="none" stroke="var(--green)" stroke-width="2.6"/></svg>
    <div class="num">03</div>
    <h3>Qualified Clinicians</h3>
    <p>Lorem ipsum dolor sit amet consectetur. Habitant venenatis sit laoreet faucibus semper ornare viverra senectus. Bibendum senectus nunc nec id enim tincidunt ut dictum.</p>
  </div>
</section>

<section class="nourish">
  <svg class="abs" style="left:0;top:0" width="1200" height="500" viewBox="0 0 1200 500">
    <defs>
      <linearGradient id="manPhoto" x1="0" y1="0" x2="1" y2="1">
        <stop offset="0" stop-color="#c9d2dc"/><stop offset=".5" stop-color="#8fa6c6"/><stop offset="1" stop-color="#b49a80"/>
      </linearGradient>
    </defs>
    <rect x="0" y="56" width="1200" height="444" fill="var(--green)"/>
    <rect x="1036" y="16" width="118" height="150" fill="#eef0f3" role="img" aria-label="Decorative dotted pattern"/>
    <polygon points="0,0 480,0 540,56 385,500 0,500" fill="url(#manPhoto)" role="img" aria-label="Photo of a relaxed man holding a glass of water while receiving an IV drip"/>
  </svg>
  <h2><em>Nourish your body</em>, nourish<br>your soul - IV Nutrition</h2>
  <p>Our IV clinics offer nutrient therapies that can help you bounce back from dehydration, boost your immune system, and support your athletic recovery. Whether you're dealing with chronic issues like fatigue, weight gain, or inflammation, IV nutrition therapy is a chill and effective way to get you feeling your best. Plus, it can help keep future health problems at bay!</p>
  <div class="btn btn-blue" style="left:581px;top:390px;width:170px;height:37px">Book Appointment
    <svg viewBox="0 0 16 16" fill="none" stroke="#fff" stroke-width="1.6"><path d="M2 8h11M9 4l4 4-4 4"/></svg></div>
</section>

<section class="treatments">
  <h2 class="section-title" style="top:96px">Our Best Selling Treatments</h2>
  <div class="abs" style="left:1030px;top:160px;width:170px;height:760px;background:linear-gradient(180deg,#f7f8fa,#fbfbfc)" role="img" aria-label="Faint line illustration of IV drip bags"></div>
  <div class="treat-feature"></div>

  <div class="treat" style="left:144px;top:196px">
    <div class="ico"><svg viewBox="0 0 40 40" fill="none" stroke="var(--green)" stroke-width="2.2"><path d="M20 5l12 5v9c0 8-5 13-12 16C13 32 8 27 8 19v-9z"/><path d="M20 14v10M15 19h10"/></svg></div>
    <h3>Immune Resilience Drips</h3>
    <p>Lorem ipsum dolor sit amet consectetur. Vel elementum tincidunt lectus tellus non tellus tincidunt.</p>
    <div class="more">Learn More <svg width="12" height="12" viewBox="0 0 16 16" fill="none" stroke="currentColor" stroke-width="1.6"><path d="M2 8h11M9 4l4 4-4 4"/></svg></div>
  </div>
  <div class="treat" style="left:461px;top:176px">
    <div class="ico"><svg viewBox="0 0 40 40" fill="none" stroke="var(--green)" stroke-width="2.2"><path d="M12 30v-6c-3-2-5-6-4-10 1-6 6-9 12-9 7 0 12 5 12 11 0 3-2 5-3 6l1 5h-4v3z"/><circle cx="21" cy="16" r="4"/></svg></div>
    <h3>Energy and Brain Power Drips</h3>
    <p>Lorem ipsum dolor sit amet consectetur. Vel elementum tincidunt lectus tellus non tellus tincidunt.</p>
    <div class="more">Learn More <svg width="12" height="12" viewBox="0 0 16 16" fill="none" stroke="currentColor" stroke-width="1.6"><path d="M2 8h11M9 4l4 4-4 4"/></svg></div>
  </div>
  <div class="treat" style="left:793px;top:200px">
    <div class="ico"><svg viewBox="0 0 40 40" fill="var(--green)"><path d="M17 8c-6 8-9 13-9 17a9 9 0 0018 0c0-4-3-9-9-17z"/><path d="M28 16c-3 4-4 6-4 8a4 4 0 008 0c0-2-1-4-4-8z" fill="#fff"/></svg></div>
    <h3 style="margin-top:20px">Hydration</h3>
    <p style="margin-top:2px">Lorem ipsum dolor sit amet consectetur. Vel elementum tincidunt lectus tellus non tellus tincidunt.</p>
    <div class="more">Learn More <svg width="12" height="12" viewBox="0 0 16 16" fill="none" stroke="currentColor" stroke-width="1.6"><path d="M2 8h11M9 4l4 4-4 4"/></svg></div>
  </div>

  <div class="vline" style="left:407px;top:500px;height:248px"></div>
  <div class="vline" style="left:743px;top:500px;height:248px"></div>

  <div class="treat" style="left:148px;top:496px">
    <div class="ico"><svg viewBox="0 0 40 40" fill="none" stroke="var(--green)" stroke-width="2.6" stroke-linecap="round"><circle cx="24" cy="9" r="3" fill="var(--green)"/><path d="M14 18l6-4 5 5-4 6 4 7M20 14l-3 8-7 3M25 19l6 1"/></svg></div>
    <h3>Athletic Performance Drips</h3>
    <p>Lorem ipsum dolor sit amet consectetur. Vel elementum tincidunt lectus tellus non tellus tincidunt.</p>
  </div>
  <div class="treat" style="left:461px;top:496px">
    <div class="ico"><svg viewBox="0 0 40 40" fill="none" stroke="var(--green)" stroke-width="2.2"><circle cx="20" cy="18" r="9"/><path d="M11 16c3-6 15-6 18 0M10 34c2-5 6-7 10-7s8 2 10 7"/></svg></div>
    <h3>Natural Beauty Drips</h3>
    <p>Lorem ipsum dolor sit amet consectetur. Vel elementum tincidunt lectus tellus non tellus tincidunt.</p>
  </div>
  <div class="treat" style="left:797px;top:504px">
    <div class="ico"><svg viewBox="0 0 40 40" fill="none" stroke="var(--green)" stroke-width="2.2"><rect x="10" y="12" width="20" height="22" rx="3"/><path d="M16 12V7h8v5"/><path d="M20 18v10M16 22l4-4 4 4"/></svg></div>
    <h3>Weight Loss Drips</h3>
    <p>Lorem ipsum dolor sit amet consectetur. Vel elementum tincidunt lectus tellus non tellus tincidunt.</p>
  </div>

  <div class="cta-line"></div>
  <div class="cta-text">Schedule an Online Consultation Today!</div>
  <div class="btn btn-green" style="left:876px;top:864px;width:170px;height:36px">Book Appointment
    <svg viewBox="0 0 16 16" fill="none" stroke="#fff" stroke-width="1.6"><path d="M2 8h11M9 4l4 4-4 4"/></svg></div>
</section>

<section class="benefits">
  <svg class="abs" style="left:0;top:0" width="1200" height="599" viewBox="0 0 1200 599">
    <defs>
      <linearGradient id="benefitPhoto" x1="0" y1="0" x2="1" y2="0">
        <stop offset="0" stop-color="#c8d0dc"/><stop offset=".35" stop-color="#a9b7cf"/><stop offset=".58" stop-color="#3d58ac"/><stop offset=".72" stop-color="var(--blue)"/>
      </linearGradient>
    </defs>
    <rect width="1200" height="599" fill="url(#benefitPhoto)" role="img" aria-label="Photo of a smiling woman adjusting an IV drip bag in a bright clinic"/>
  </svg>
  <h2><em>Benefits</em> IV Theraphy</h2>
  <p class="intro">IV Therapy is the fastest way to deliver essential nutrients throughout the body because it bypasses the digestive system and goes directly into the bloodstream, resulting in a much higher absorption rate – 90% – 100%.</p>
  <div class="acc open" style="top:218px">Immediate Effect
    <svg viewBox="0 0 16 16" fill="none" stroke="currentColor" stroke-width="1.6"><path d="M3 10l5-5 5 5"/></svg></div>
  <p class="acc-body">IV infusions deliver minerals and nutrients directly into the bloodstream, ensuring 100% absorption compared to 50-60% for oral intake. This method provides immediate effects, boosting the body's regeneration and repair processes.</p>
  <div class="acc" style="top:378px">Better Hydration
    <svg viewBox="0 0 16 16" fill="none" stroke="currentColor" stroke-width="1.6"><path d="M3 6l5 5 5-5"/></svg></div>
  <div class="acc" style="top:432px">More Nutrients
    <svg viewBox="0 0 16 16" fill="none" stroke="currentColor" stroke-width="1.6"><path d="M3 6l5 5 5-5"/></svg></div>
</section>

<section class="testimonials">
  <h2 class="section-title" style="top:78px">What Our Clients Have to Say</h2>
  <svg class="arrow" style="left:66px" viewBox="0 0 24 36" fill="none" stroke="var(--blue)" stroke-width="3"><path d="M17 6L7 18l10 12"/></svg>
  <svg class="arrow" style="left:1110px;top:274px" viewBox="0 0 24 36" fill="none" stroke="var(--blue)" stroke-width="3"><path d="M7 6l10 12L7 30"/></svg>

  <div class="t-card" style="left:119px">
    <div class="t-top"><span class="stars">★★★★★</span><span class="t-badge"><i></i>Testimonial</span></div>
    <p>Dude, your stuff is the bomb! House rent is the real deal! I STRONGLY recommend house rent to EVERYONE interested in running a successful online business!</p>
    <div class="t-author"><i></i>Mira Castell</div>
  </div>
  <div class="t-card" style="left:449px">
    <div class="t-top"><span class="stars">★★★★★</span><span class="t-badge"><i></i>Testimonial</span></div>
    <p style="margin-top:14px">"I like Harborline Estate more and more each day because it makes my life a lot easier. We can't understand how we've been living without Harborline Estate. Harborline Estate has got everything I need. The service was excellent."</p>
    <div class="t-author"><i></i>Mrs. Oduya</div>
  </div>
  <div class="t-card" style="left:779px">
    <div class="t-top"><span class="stars">★★★★★</span><span class="t-badge"><i></i>Testimonial</span></div>
    <p style="margin-top:30px">You've saved our business! Harborline Estate has got everything I need. We were treated like royalty. It's really wonderful.</p>
    <div class="t-author"><i></i>Tomas Reyland</div>
  </div>
</section>

<section class="contact">
  <div class="abs" style="left:0;top:330px;width:540px;height:342px;background:linear-gradient(180deg,#ffffff,#f6f7f9)" role="img" aria-label="Faint line illustration of a hand and an IV drip bag"></div>
  <h2>Find the right IV drip or<br>booster <span>to support your<br>health goals</span></h2>
  <h4>Our Locations</h4>
  <div class="info" style="left:117px;top:343px">
    <svg viewBox="0 0 18 18" fill="none" stroke="var(--green)" stroke-width="1.5"><path d="M9 16s5-5 5-9a5 5 0 00-10 0c0 4 5 9 5 9z"/><circle cx="9" cy="7" r="2"/></svg>
    <div>482 Calloway Ave<br>Los Angeles, CA 90049</div>
  </div>
  <div class="info" style="left:117px;top:406px">
    <svg viewBox="0 0 18 18" fill="none" stroke="var(--green)" stroke-width="1.5"><circle cx="9" cy="9" r="7"/><path d="M9 5v4l3 2"/></svg>
    <div>Monday – Saturday 10:00 am – 6:00 pm<br>Sunday – Closed</div>
  </div>
  <div class="info" style="left:117px;top:468px">
    <svg viewBox="0 0 18 18" fill="none" stroke="var(--green)" stroke-width="1.5"><path d="M4 2l3 3-2 2c1 2 3 4 5 5l2-2 3 3-2 3C8 16 2 10 1 4z"/></svg>
    <div>424-555-0182</div>
  </div>

  <div class="abs" style="left:1050px;top:46px;width:120px;height:150px;background:#eef3e6" role="img" aria-label="Decorative dotted pattern"></div>
  <div class="form-box">
    <h3>Schedule an Online<br>Consultation Today!</h3>
    <div class="field" style="top:170px">Your Full Name</div>
    <div class="field" style="top:230px">Email Address</div>
    <div class="field" style="top:291px">Phone Number</div>
    <div class="field" style="top:348px;height:120px">Message</div>
    <div class="btn btn-blue" style="left:66px;top:493px;width:387px;height:36px;font-size:12px">BOOK NOW
      <svg viewBox="0 0 16 16" fill="none" stroke="#fff" stroke-width="1.6"><path d="M2 8h11M9 4l4 4-4 4"/></svg></div>
  </div>
</section>

<footer class="footer">
  <div class="brand" style="left:117px;top:76px;color:var(--white)">Velmo<i></i></div>
  <h5 style="left:117px;top:172px">CONNECT WITH US</h5>
  <div class="social" aria-label="Social media links"><i></i><i></i><i></i></div>

  <h5 style="left:498px;top:82px">QUICKLINKS</h5>
  <div class="link" style="top:122px;color:var(--green)">Home</div>
  <div class="link" style="top:153px">About Us</div>
  <div class="link" style="top:185px">Treatment</div>
  <div class="link" style="top:216px">Treatments</div>
  <div class="link" style="top:248px">Contact</div>

  <h5 style="left:692px;top:82px">OUR LOCATIONS</h5>
  <div class="info" style="left:692px;top:120px;color:var(--white)">
    <svg viewBox="0 0 18 18" fill="none" stroke="var(--green)" stroke-width="1.5"><path d="M9 16s5-5 5-9a5 5 0 00-10 0c0 4 5 9 5 9z"/><circle cx="9" cy="7" r="2"/></svg>
    <div>482 Calloway Ave<br>Los Angeles, CA 90049</div>
  </div>
  <div class="info" style="left:692px;top:184px;color:var(--white)">
    <svg viewBox="0 0 18 18" fill="none" stroke="var(--green)" stroke-width="1.5"><circle cx="9" cy="9" r="7"/><path d="M9 5v4l3 2"/></svg>
    <div>Monday – Saturday 10:00 am – 6:00 pm<br>Sunday – Closed</div>
  </div>
  <div class="info" style="left:692px;top:244px;color:var(--white)">
    <svg viewBox="0 0 18 18" fill="none" stroke="var(--green)" stroke-width="1.5"><path d="M4 2l3 3-2 2c1 2 3 4 5 5l2-2 3 3-2 3C8 16 2 10 1 4z"/></svg>
    <div>424-555-0182</div>
  </div>

  <div class="rule"></div>
  <div class="copy">© 2025 Velmo Hydration All Rights Reserved</div>
</footer>

</body>
</html>
```